Tri Fold - Restaurant Brochure & pdf multipage

Develop a product guide specific to "restaurant owners" for our company's restaurant insurance services. It will need to be eye-catching, personal, unique, and industry-specific. Several Insurance flyers from our companies are attached for review. We are happy to provide guidance along the way. Our website is www.kovalenbrokerage.example. Please grab logos etc. from there. We can provide other files and more detailed copy.

Target Market(s)

Restaurant owners and CFO's

Industry/Entity Type

Insurance Broker

Font styles to use
Other font styles liked:
• match website fonts

Requirements
Must have
• WE WILL PROVIDE DETAILED CONTENT! AT THIS TIME WE ARE LOOKING FOR THE BASIC DESIGN AND LAYOUT.

EYE-CATCHING MODERN DESIGN WITH IMAGES AND BRANDED FEEL. must be print-ready and set up as a PDF to email.

brief description of our agency and its personal boutique feel specializing in the restaurant market. Also, offer a full-service solution to no only manage their business but personal risks too.

Coverages that need to be listed with a brief description: (See attached Flyers)
General Liability
FF&E (Furniture, Fixtures, and Equipment), Property
Workers Compensation
Umbrella
Liquor Liability
Auto
Cyber
Bonds
EPLI

Carrier List:
The Wexmoor
Bastion
Ferrow Common
Wayfarers
Plains Motor
Quorra
DELVA
Holloway
CountyFirst
KTO
And many more
Nice to have
• carrier logos if room.
Should not have
• TO BE DETERMINED.

```html
<!DOCTYPE html>
<html lang="en">
<head>
<meta charset="utf-8">
<title>Kovalen Brokerage – Restaurant Insurance Brochure</title>
<link rel="stylesheet" href="https://fonts.googleapis.com/css2?family=Cinzel:wght@400;600;700&family=Arimo:ital,wght@0,400;0,700;1,400&display=swap">
<style>
:root{
  --red:#e3211c;
  --red-deep:#c41610;
  --ink:#1c1c1f;
  --paper:#ffffff;
  --canvas:#eeeeef;
  --rule:#c9c9c9;
  --muted:#4a4a4a;
}
*{box-sizing:border-box;margin:0;padding:0}
html,body{width:1200px;height:1200px;overflow:hidden;background:var(--canvas)}
body{font-family:"Arimo",Arial,sans-serif;color:var(--ink);position:relative}
.page{position:absolute;top:354px;width:380px;height:492px;background:var(--paper);overflow:hidden;box-shadow:0 4px 14px rgba(0,0,0,.18)}
.page--cover{left:18px}
.page--coverages{left:410px}
.page--options{left:802px}
.photo{position:absolute}

/* invented agency name, set as plain text */
.agency-name{position:absolute;font-family:"Arimo",Arial,sans-serif;font-weight:700;color:#fff;white-space:nowrap}
.agency-name--cover{top:46px;left:0;width:380px;text-align:center;font-size:22px}
.agency-name--hero{top:104px;left:18px;font-size:9px;line-height:1.2}

/* cover */
.cover-photo{inset:0;background:linear-gradient(120deg,#3a2a22 0%,#17171c 35%,#1c1d26 65%,#4a4744 100%)}
.welcome{position:absolute;left:26px;top:142px;width:228px;height:228px;border-radius:50%;background:rgba(227,33,28,.94);color:#fff;padding:50px 26px 0 34px}
.welcome h1{font-family:"Cinzel",serif;font-weight:600;font-size:11px;letter-spacing:.4px}
.welcome h1::after{content:"";display:block;width:20px;height:1.5px;background:#fff;margin:4px 0 7px}
.welcome p{font-size:6px;line-height:1.35;margin-bottom:5px}

/* interior headers */
.hero{position:absolute;left:0;top:0;width:380px;height:200px}
.hero--bistro{background:linear-gradient(100deg,#2b3a2e 0%,#1f2a25 45%,#3c4a48 70%,#27312e 100%)}
.hero--table{background:linear-gradient(160deg,#2a211c 0%,#3d2e22 55%,#6b4e33 78%,#2a211c 100%)}
.ribbon{position:absolute;top:0;left:26px;width:38px;height:78px;background:var(--red)}
.ribbon::after{content:"";position:absolute;left:0;bottom:-12px;border-left:19px solid var(--red);border-right:19px solid var(--red);border-bottom:12px solid transparent}
.carrier{position:absolute;top:132px;left:18px;font-family:"Arimo",Arial,sans-serif;font-weight:700;font-size:6px;color:#fff}
.hero-title{position:absolute;font-family:"Cinzel",serif;color:#fff;font-weight:600;line-height:1.12}
.hero-title--advisors{left:112px;top:92px;font-size:15px}
.hero-title--advisors span{display:block;font-family:"Arimo",sans-serif;font-weight:400;font-size:11px;margin-top:2px}
.hero-title--serve{left:118px;top:74px;font-size:15px;letter-spacing:.3px}

/* coverages page */
.interior-photo{left:14px;top:216px;width:156px;height:250px;background:linear-gradient(180deg,#8c8580 0%,#5a4f46 40%,#2e2a27 100%)}
.section-title{font-family:"Cinzel",serif;font-weight:600;font-size:9.5px;line-height:1.1;color:var(--ink)}
.section-title::after{content:"";display:block;width:18px;height:1.5px;background:var(--red);margin-top:3px}
.coverages{position:absolute;left:180px;top:214px;width:188px}
.coverage-table{width:100%;border-collapse:collapse;margin-top:6px}
.coverage-table td{font-size:5.1px;line-height:1.25;padding:2.6px 0;border-bottom:.6px solid var(--rule);vertical-align:top}
.coverage-table td:first-child{width:54px;color:var(--muted);padding-right:4px}
.coverage-table tr:last-child td{border-bottom:1.2px solid var(--red)}
.page-rule{position:absolute;left:0;bottom:12px;width:300px;height:3px;background:var(--red)}

/* options page */
.why{position:absolute;left:14px;top:214px;width:150px;height:262px;background:linear-gradient(180deg,#2b2624 0%,#3b332d 100%);color:#fff;padding:10px 9px}
.why h2{font-family:"Cinzel",serif;font-weight:600;font-size:8px;margin-bottom:5px}
.why h2.bop{margin-top:8px}
.why p,.why li{font-size:4.8px;line-height:1.3;margin-bottom:3px}
.why .caps{text-transform:uppercase}
.why ul{list-style:none}
.why li::before{content:"• ";color:var(--red)}
.why strong{color:var(--red);font-weight:700}
.options{position:absolute;left:174px;top:214px;width:196px}
.options .section-title{font-size:8.5px}
.options p{font-size:4.8px;line-height:1.3;margin-top:4px}
.options strong{color:var(--red-deep)}
</style>
</head>
<body>

<section class="page page--cover" aria-label="Brochure cover">
  <div class="photo cover-photo" role="img" aria-label="Overhead photo of a restaurant table with two plated salads and a glass of red wine"></div>
  <div class="agency-name agency-name--cover">Kovalen Brokerage</div>
  <div class="welcome">
    <h1>WELCOME TO KOVALEN</h1>
    <p>Kovalen Brokerage believes in the ability of people to take control of their lives and of their future. Among the countless insurance companies in Georgia, Kovalen Brokerage stands out as the independently owned risk management firm that does not shy away from utilizing its autonomy to better serve the people.</p>
    <p>Your organization can depend on the vast number of carriers we work with—all A-rated or better. Our team can lend you the skills and experience necessary to design an insurance plan that suits the specific needs of your business. Trust us to deliver risk management strategies that are as unique as your business and as effective as you want them to be.</p>
  </div>
</section>

<section class="page page--coverages" aria-label="Standard coverages page">
  <div class="hero hero--bistro" role="img" aria-label="Photo of a restaurant owner in an apron standing at the glass door of his bistro"></div>
  <div class="ribbon"></div>
  <div class="agency-name agency-name--hero">Kovalen<br>Brokerage</div>
  <h2 class="hero-title hero-title--advisors">INDEPENDENT<br>RISK ADVISORS<span>For your Restaurant</span></h2>

  <div class="photo interior-photo" role="img" aria-label="Photo of a restaurant dining room with round pendant lamps and plants"></div>
  <div class="coverages">
    <h3 class="section-title">STANDARD COVERAGES<br>FOR YOUR BUSINESS</h3>
    <table class="coverage-table">
      <tr><td>General Liability</td><td>Covers legal liability associated with your business operations, including bodily harm to other people or damage to their property</td></tr>
      <tr><td>FF&amp;E, Property</td><td>Covers your business-owned buildings and business personal property from damages caused by a covered loss, such as fire, storms, vandalism, theft or water damage</td></tr>
      <tr><td>Workers Compensation</td><td>Helps cover medical expenses, lost wages and return to work support for employees who are injured on the job</td></tr>
      <tr><td>Umbrella</td><td>Provides additional protection above your commercial auto and general liability limits in the event of a large claim or lawsuit</td></tr>
      <tr><td>Liquor Liability</td><td>Protects against lawsuits resulting from overconsumption, whether or not the incident occurred on your premises</td></tr>
      <tr><td>Auto</td><td>Extends liability coverage to include property damage and/or injury resulting from parking a vehicle not owned, rented or loaned by your business</td></tr>
      <tr><td>Cyber</td><td>Covers the cost of notifying affected individuals, managing public relations and securing legal defense if sensitive data is hacked, lost or stolen, and helps cover costs associated with lawsuits against you that may arise from a data breach</td></tr>
      <tr><td>Bonds</td><td>Covers lost or damaged business personal property, including money and securities, as a result of dishonest acts committed by your employees</td></tr>
      <tr><td>EPLI</td><td>Covers employment-related lawsuits, such as wrongful termination, harassment, coercion or discrimination</td></tr>
    </table>
  </div>
  <div class="page-rule"></div>
</section>

<section class="page page--options" aria-label="Optional coverages page">
  <div class="hero hero--table" role="img" aria-label="Photo of a set wooden restaurant table with plates and napkins"></div>
  <div class="ribbon"></div>
  <div class="agency-name agency-name--hero">Kovalen<br>Brokerage</div>
  <div class="carrier">The Wexmoor</div>
  <h2 class="hero-title hero-title--serve">YOU WORK HARD<br>SERVING OTHERS,<br>HERE'S HOW WE CAN<br>SERVE YOU.</h2>

  <div class="why">
    <h2>WHY THE WEXMOOR?</h2>
    <p class="caps">We work to earn your trust and confidence with every interaction.</p>
    <p>Customers rate us highly for a fast, fair and friendly claim experience.</p>
    <p>Small business owners across the country trust The Wexmoor to insure their business.</p>
    <p>We're an A-rated carrier with a long record of standing by restaurants when it matters.</p>
    <h2 class="bop">BUSINESS OWNER'S POLICY (BOP)</h2>
    <p>A BOP can help protect your business in much the same way that a homeowners policy protects your home and personal possessions. The Wexmoor's BOP combines these essential coverages to provide a cost-effective solution to help safeguard your restaurant:</p>
    <ul>
      <li><strong>Business Property Insurance</strong> to help protect the property you own, lease or rent</li>
      <li><strong>Business Liability coverage</strong> to help protect your business in the event it is responsible for causing harm to a person and/or damage to property</li>
      <li><strong>Business Income coverage</strong> to help protect lost income if your business is forced to close due to direct physical loss or damage to its premises resulting from a covered cause of loss</li>
    </ul>
  </div>

  <div class="options">
    <h3 class="section-title">EXAMPLES OF À LA CARTE<br>COVERAGES RESTAURANTS<br>LIKE YOURS SELECT</h3>
    <p>A wide range of optional coverages offer additional protection for risks that are unique to restaurants. Many are available separately or in cost-effective packages, giving you the flexibility to design a program that's important to your business.</p>
    <p><strong>Data Breach</strong> helps you pay for response expenses, legal costs and income protection if the sensitive personal information you collect or store is lost or stolen.</p>
    <p><strong>Employment Practices Liability (EPL)</strong> provides coverage if you're sued by an employee, patron or vendor alleging discrimination, sexual harassment, wrongful termination or other types of claims relating to your employment practices.</p>
    <p><strong>Liquor Liability</strong> helps cover your legal costs, court fees and any civil or criminal damages resulting from the sale of liquor at your restaurant.</p>
    <p><strong>Franchise Upgrade</strong> helps pay additional costs a franchisee may incur to upgrade damaged property to franchise standards following a covered loss.</p>
    <p><strong>Business Income for Food Contamination</strong> provides coverage for lost income if your operations are suspended by a public health authority due to the discovery of food contamination.</p>
    <p><strong>Business Income for Cloud Service Interruption</strong> helps pay for lost income if you need to suspend or slow business operations because of an unplanned and unannounced interruption in your cloud service.</p>
    <p><strong>Employee Dishonesty</strong> provides coverage if an employee steals money, securities or other property owned by your business.</p>
    <p><strong>Spoilage</strong> provides coverage for the cost of food or income that's lost due to a breakdown or failure of heating or cooling equipment, power failure or contamination by a refrigerant.</p>
    <p><strong>Electronic Data and Interruption of Computer Operations</strong> pays to replace or restore electronic data that has been destroyed, corrupted, or made inaccessible by a computer virus or covered loss, and any loss of business income.</p>
  </div>
  <div class="page-rule"></div>
</section>

</body>
</html>
```